Brickline Gains Online Redesign

The company needs a new online presence built that better represents who we are and what we do. Our online presence needs to be optimised for both PC, tablet and Phone usage.

Our existing site; www.bricklinegains.com.au - this page currently forwards to one of our sales pages.
The entire site needs to be redesigned along with the sales pages /workshop and /faststart

Here are our competition:
https://www.coraltemsby.com/
http://quorvahomeschooling.com.au/property-education-experts/coral-temsby/
http://harrietvolonsky.com.au/
www.refitforyield.com.au/
http://fullmanualtorefurb.com.au/

Target Market(s)

40-55 Husband and Wife with children that are busy profesionals with a family income of 150-300k PA with 2-3 kids

Industry/Entity Type

Education

Number of Pages Required

5+ page

Font styles to use
Sans Serif
Script

Colors

Designer to choose colors to be used in the design.

Requirements
Must have
• Main Page
• Events Page
• Media Page
• Past Projects
• Blog - plesae design a template blog; both individual blogs and library (i like this http://bram.blog/)
• eBooks page
• Shopping Cart - buy eBooks, eBook Packs and courses
• eBook download page for each eBook
• Testimonials
• Event Sales Page
• 2 hr Event - currently www.bricklinegains.com.au/workshop & /faststart & /faststartv
Nice to have
• A few different options for sales landing pages to sell the 2 hr event
• A few different blog templates - video, text, infographic etc
• The business is a Property Educatiom, Mentoring and Consulting Company
Should not have
• This is not a real estate sales business

```html
<!DOCTYPE html>
<html lang="en">
<head>
<meta charset="utf-8">
<title>Renovating Property for Profit Workshop – Brickline Gains</title>
<link href="https://fonts.googleapis.com/css2?family=Montserrat:wght@400;500;600;700&family=Open+Sans:wght@400;600&display=swap" rel="stylesheet">
<style>
:root{
  --blue:#1e5a9e;
  --navy:#16294a;
  --orange:#d07a28;
  --ink:#333a44;
  --muted:#6b7280;
  --light:#f6f6f6;
  --line:#e3e3e3;
  --white:#ffffff;
}
*{box-sizing:border-box;margin:0;padding:0}
html,body{width:1200px;height:3947px;overflow:hidden;background:var(--white)}
body{font-family:"Open Sans",Arial,sans-serif;color:var(--ink);position:relative}
h1,h2,h3,.heading{font-family:"Montserrat",Arial,sans-serif}
section,header,footer{position:relative;width:1200px}
.abs{position:absolute}
.btn{position:absolute;display:flex;align-items:center;justify-content:center;border-radius:30px;color:var(--white);font-family:"Montserrat",Arial,sans-serif;font-weight:700;text-decoration:none}
.btn-orange{background:var(--orange)}
.btn-blue{background:var(--blue)}
.brand{display:flex;align-items:center;gap:8px;font-family:"Montserrat",Arial,sans-serif;font-weight:700;color:var(--blue);font-size:20px}
.brand-mark{width:14px;height:14px;background:var(--orange)}

/* header */
.site-header{height:100px;background:var(--white)}
.site-header .brand{left:197px;top:36px;position:absolute}
.nav{position:absolute;top:0;left:384px;height:100px;display:flex;align-items:center;font-family:"Montserrat",Arial,sans-serif;font-size:13px;font-weight:600;color:var(--ink)}
.nav a{color:var(--ink);text-decoration:none;position:absolute;white-space:nowrap}
.nav a.active::after{content:"";position:absolute;left:0;right:0;bottom:-8px;height:2px;background:var(--orange)}
.header-phone{position:absolute;left:842px;top:40px;display:flex;align-items:center;gap:8px;font-family:"Montserrat",Arial,sans-serif;font-size:12.5px;font-weight:600}

/* hero */
.hero{height:542px;background:linear-gradient(90deg,#1b3d6e 0%,#24508a 48%,#2c5c93 50%,#4d6f98 100%)}
.hero-title{left:197px;top:262px;width:360px;color:var(--white);font-size:31px;font-weight:700;line-height:40px;position:absolute}
.hero-meta{left:197px;color:var(--white);font-size:12.5px;position:absolute}
.hero-price{left:197px;top:402px;color:var(--white);font-family:"Montserrat",Arial,sans-serif;font-weight:700;font-size:24px;position:absolute}
.hero-note{left:203px;top:416px;color:#d8e0ec;font-size:9.5px;position:absolute}

/* welcome */
.welcome{height:373px}
.welcome h2{position:absolute;left:205px;top:57px;color:var(--orange);font-size:24px;font-weight:700}
.welcome p{position:absolute;left:205px;top:100px;width:352px;font-size:11.5px;line-height:21.5px;color:var(--ink)}
.welcome .photo{position:absolute;left:597px;top:0;width:603px;height:373px;background:linear-gradient(160deg,#8fa9c5 0%,#6d6b6e 45%,#5b3a2e 100%)}

/* topics */
.topics{height:221px}
.section-title{position:absolute;left:0;width:1200px;text-align:center;font-family:"Montserrat",Arial,sans-serif;font-weight:700;font-size:24px}
.topics .section-title{top:58px;color:var(--blue)}
.topic{position:absolute;top:133px;width:240px;font-size:13.5px;line-height:24px;color:var(--ink)}
.topic.active{color:var(--orange)}
.topic-divider{position:absolute;top:132px;width:1px;height:54px;background:var(--line)}

/* results band */
.results{height:276px;background:linear-gradient(180deg,#142a4f,#1f3f6c 60%,#2a4d7a)}
.results .notch{position:absolute;left:232px;top:0}
.results .lead{position:absolute;top:62px;left:0;width:1200px;text-align:center;color:var(--white);font-family:"Montserrat",Arial,sans-serif;font-weight:700;font-size:14.5px}
.results .sub{position:absolute;top:100px;left:300px;width:600px;text-align:center;color:#e3e9f2;font-size:15px;line-height:27px}

/* reports */
.reports{height:348px}
.reports .section-title{top:70px;color:var(--blue)}
.report-col{position:absolute;top:145px;width:240px;list-style:none}
.report-col li{position:relative;padding-left:18px;font-size:10px;line-height:15px;margin-bottom:12px;color:var(--muted)}
.report-col li::before{content:"";position:absolute;left:0;top:7px;width:6px;height:1px;background:var(--orange)}

/* instructor */
.instructor{height:552px;background:var(--light)}
.instructor .section-title{top:74px;color:var(--orange)}
.portrait{position:absolute;left:205px;top:153px;width:226px;height:226px;border-radius:50%;border:5px solid var(--orange);background:linear-gradient(180deg,#dcdfe3,#9aa3ad 60%,#26303c)}
.instructor h3{position:absolute;left:468px;top:188px;color:var(--blue);font-size:14px;font-weight:700}
.instructor p{position:absolute;left:468px;top:222px;width:585px;font-size:11px;line-height:23px;color:var(--muted)}
.arrow{position:absolute}

/* faq */
.faq{height:350px}
.faq .section-title{top:70px;color:var(--orange)}
.faq-item{position:absolute;top:158px;width:375px}
.faq-item h3{color:var(--blue);font-size:13.5px;font-weight:700;margin-bottom:14px}
.faq-item p{font-size:10.5px;line-height:20px;color:var(--muted)}

/* contact band */
.contact-band{height:142px;background:var(--orange);color:var(--white);text-align:center;font-family:"Montserrat",Arial,sans-serif}
.contact-band .l1{position:absolute;top:40px;width:1200px;font-size:19px;font-weight:700}
.contact-band .l2{position:absolute;top:72px;width:1200px;font-size:19px;font-weight:400}

/* testimonial */
.testimonial{height:376px}
.testimonial h2{position:absolute;top:97px;width:1200px;text-align:center;color:var(--blue);font-size:29px;font-weight:700}
.testimonial .when{position:absolute;top:135px;width:1200px;text-align:center;font-size:10px;color:var(--muted)}
.testimonial .rule{position:absolute;top:164px;left:581px;width:38px;height:2px;background:var(--orange)}
.testimonial blockquote{position:absolute;top:194px;left:235px;width:730px;text-align:center;font-size:14px;line-height:28px;color:var(--ink)}

/* map */
.map{height:428px;background:linear-gradient(135deg,#dfe8d5 0%,#ece9e2 40%,#e8e4dc 70%,#d7e3cc 100%)}

/* footer */
.site-footer{height:197px}
.site-footer .brand{position:absolute;left:197px;top:75px}
.foot-col{position:absolute;top:52px}
.foot-col h4{font-family:"Montserrat",Arial,sans-serif;color:var(--blue);font-size:12px;font-weight:700;margin-bottom:14px}
.foot-row{display:flex;align-items:center;gap:10px;font-size:11px;color:var(--ink);margin-bottom:13px}
.partners{position:absolute;left:843px;top:94px;width:160px;text-align:center;font-size:11px}
.partner-badges{position:absolute;left:870px;top:118px;display:flex;gap:10px}
.partner-badges span{display:block;width:44px;height:26px;background:#c9cfd8;border-radius:3px}
.partner-badges span:nth-child(2){background:var(--blue)}
.legal{position:absolute;left:0;top:3905px;width:1200px;height:42px;border-top:1px solid var(--line);font-size:10px;color:var(--muted);display:flex;align-items:center;justify-content:center}
.legal .page{position:absolute;right:34px}
</style>
</head>
<body>

<header class="site-header">
  <div class="brand"><span class="brand-mark"></span>Brickline Gains</div>
  <nav class="nav">
    <a class="active" style="left:0;top:44px">Home</a>
    <a style="left:68px;top:44px">Blog</a>
    <a style="left:134px;top:44px">E-Books</a>
    <a style="left:216px;top:44px">Contact Us</a>
  </nav>
  <a class="btn btn-blue" style="left:689px;top:36px;width:134px;height:30px;font-size:12px">Book My Seat</a>
  <div class="header-phone">
    <svg width="18" height="18" viewBox="0 0 24 24"><path d="M6.6 10.8c1.4 2.8 3.8 5.1 6.6 6.6l2.2-2.2c.3-.3.7-.4 1-.2 1.1.4 2.3.6 3.6.6.6 0 1 .4 1 1V20c0 .6-.4 1-1 1C10.6 21 3 13.4 3 4c0-.6.4-1 1-1h3.5c.6 0 1 .4 1 1 0 1.3.2 2.5.6 3.6.1.3 0 .7-.2 1z" fill="none" stroke="#d07a28" stroke-width="1.6"/></svg>
    Ask a question&nbsp; 1300 555 014
  </div>
</header>

<section class="hero" role="img" aria-label="Workshop presenter photo under a deep blue overlay">
  <h1 class="hero-title">Renovating Property for Profit Workshop</h1>
  <div class="hero-meta" style="top:356px"><strong>Event Details:</strong> Tuesday 2nd May 2017 at 7pm to 9pm –</div>
  <div class="hero-meta" style="top:315px;position:absolute;top:312px;display:none"></div>
  <div class="hero-meta" style="top:312px;display:none"></div>
  <div class="hero-meta" style="top:312px;display:none"></div>
  <div class="hero-meta" style="top:312px;display:none"></div>
  <div class="hero-meta" style="top:312px;display:none"></div>
  <div class="hero-meta" style="top:312px;display:none"></div>
  <div class="hero-meta" style="top:312px;display:none"></div>
  <div class="hero-meta" style="top:312px;display:none"></div>
  <div class="hero-meta" style="top:312px;display:none"></div>
  <div class="hero-meta" style="top:312px;display:none"></div>
  <div class="hero-meta" style="top:312px;display:none"></div>
  <div class="hero-meta" style="top:312px;display:none"></div>
  <div class="hero-meta" style="top:312px;display:none"></div>
  <div class="hero-meta" style="top:312px;display:none"></div>
  <div class="hero-meta" style="top:312px;display:none"></div>
  <div class="hero-meta" style="top:312px;display:none"></div>
  <div class="hero-meta" style="top:312px;display:none"></div>
  <div class="hero-meta" style="top:312px;display:none"></div>
  <div class="hero-meta" style="top:312px;display:none"></div>
  <div class="hero-meta" style="top:312px;display:none"></div>
  <div class="hero-meta" style="top:312px;display:none"></div>
  <div class="hero-meta" style="top:312px;display:none"></div>
  <div class="hero-meta" style="top:312px;display:none"></div>
  <div class="hero-meta" style="top:312px;display:none"></div>
  <div class="hero-meta" style="top:312px;display:none"></div>
  <div class="hero-meta" style="top:312px;display:none"></div>
  <div class="hero-meta" style="top:312px;display:none"></div>
  <div class="hero-meta" style="top:312px;display:none"></div>
  <div class="hero-meta" style="top:312px;display:none"></div>
  <div class="hero-meta" style="top:312px;display:none"></div>
  <div class="hero-meta" style="top:312px;display:none"></div>
  <div class="hero-meta" style="top:312px;display:none"></div>
  <div class="hero-meta" style="top:312px;display:none"></div>
  <div class="hero-meta" style="top:312px;display:none"></div>
  <div class="hero-meta" style="top:312px;display:none"></div>
  <div class="hero-meta" style="top:320px;display:none"></div>
  <div class="hero-meta" style="top:386px">Riverside Grand Parramatta</div>
  <div class="hero-price" style="top:410px">Tickets only $29</div>
  <a class="btn btn-orange" style="left:205px;top:461px;width:222px;height:44px;font-size:15px">Book My Seat Now !</a>
  <div class="hero-note" style="top:516px">**Secure Booking – Your Details are Safe**</div>
  <svg class="abs" style="left:547px;top:208px" width="96" height="96" viewBox="0 0 96 96" aria-hidden="true">
    <circle cx="48" cy="48" r="44" fill="rgba(16,30,56,.55)" stroke="#d07a28" stroke-width="4"/>
    <path d="M38 30 L66 48 L38 66 Z" fill="#fff"/>
  </svg>
</section>

<section class="welcome">
  <h2>Welcome to Brickline Gains</h2>
  <p>Learn how to significantly increase your income and live an extraordinary life in this ground up fundamentals workshop. You will learn how to select, finance and make the correct choices in renovating a property as well as the terminology used in the industry. You will also be introduced to negotiating with both agents and finance institutions along with a deep-dive look at some real world case studies. This workshop is ideal for those who seek alternative paths to true financial freedom and is perfect for people at any stage of their life – from buying their first home to looking at investing in property for their future.</p>
  <div class="photo" role="img" aria-label="Street of red brick terrace houses under a pale sky"></div>
</section>

<section class="topics">
  <h2 class="section-title">Workshop Topics Include</h2>
  <div class="topic active" style="left:197px">Recent Case Studies of Renovating for Profit</div>
  <div class="topic-divider" style="left:410px"></div>
  <div class="topic" style="left:468px">Everybody can renovate, but can Everybody Renovate for Profit?</div>
  <div class="topic-divider" style="left:715px"></div>
  <div class="topic" style="left:742px">Buying Houses in any Market and Renovate for Profit</div>
</section>

<section class="results" role="img" aria-label="Dusk view of suburban houses under a navy overlay">
  <svg class="notch" width="56" height="26" viewBox="0 0 56 26" aria-hidden="true"><path d="M0 0 H56 L28 26 Z" fill="#fff"/></svg>
  <div class="lead">Results from a system that has generated over 1.3 million dollars in profit in the last three years:</div>
  <div class="sub">Why would someone choose to renovate for profit? How can it provide a great income and lifestyle? What are the biggest mistakes we made that you can learn from?</div>
  <a class="btn btn-orange" style="left:524px;top:186px;width:152px;height:35px;font-size:12px">Read More Topics</a>
</section>

<section class="reports">
  <h2 class="section-title">You'll Receive the Following Finance &amp; Property Reports</h2>
  <ul class="report-col" style="left:197px">
    <li>"Debt Review" by Home Ledger</li>
    <li>4 "PropMetrics Data Property" reports</li>
    <li>"Top Suburbs for Renovating" reports</li>
  </ul>
  <ul class="report-col" style="left:468px">
    <li>"Best Suburbs Rental Yield" report</li>
    <li>"Australia Top Growth Performance Predictions"</li>
    <li>"NSW State Market" analysis report</li>
  </ul>
  <ul class="report-col" style="left:742px">
    <li>"NSW Growth Projections" review</li>
    <li>Brickline Gains eBook series (3 eBooks included in total)</li>
    <li>In total, you'll be receiving over $1000 worth of finance and property collateral, on top of everything you'll learn at the event!</li>
  </ul>
</section>

<section class="instructor">
  <h2 class="section-title">Workshop Instructor</h2>
  <svg class="arrow" style="left:88px;top:2128px;top:268px" width="14" height="22" viewBox="0 0 14 22" aria-hidden="true"><path d="M11 2 L3 11 L11 20" fill="none" stroke="#d07a28" stroke-width="3"/></svg>
  <svg class="arrow" style="left:1098px;top:268px" width="14" height="22" viewBox="0 0 14 22" aria-hidden="true"><path d="M3 2 L11 11 L3 20" fill="none" stroke="#d07a28" stroke-width="3"/></svg>
  <div class="portrait" role="img" aria-label="Portrait of the workshop instructor in a suit"></div>
  <h3>Warren Hale</h3>
  <p>In 1984, at just 19 years old, I began investing in property. Over the course of the past 30 years, I've invested more than $250,000 in personal development, property seminars and programs with experts in their respective fields. Before launching Brickline Gains with James, I was the CEO of a National Hydraulic Company, and before that, I managed several large business units for a corporate company. I have the experience and the education, yes, but what I'm truly driven by is educating, inspiring and empowering people how to change their lives through property.</p>
  <a class="btn btn-blue" style="left:487px;top:414px;width:226px;height:46px;font-size:15px">Book My Seat Now !</a>
</section>

<section class="faq">
  <h2 class="section-title">Frequently Asked Questions</h2>
  <div class="faq-item" style="left:197px">
    <h3>Are you selling property in this workshop?</h3>
    <p>No. This is not some "buy off the plan" or "Queensland land sale" property spruiking seminar nor are we real estate agents in disguise. This is a real, live workshop with actionable take-aways and absolutely no high pressure sell or obligation to come to any other events we hold.</p>
  </div>
  <div class="faq-item" style="left:639px">
    <h3>Why should I pay $29 to come to this workshop?</h3>
    <p>This is a face-to-face, up close and personal interactive and fully participatory training workshop designed by Australia's leading Profit from Property strategists. However if you feel in any way that this wasn't one of the best value workshops you've ever been to we are happy to refund you in full.</p>
  </div>
</section>

<section class="contact-band">
  <div class="l1">If you have any other questions you can always give us a</div>
  <div class="l2">call on 1300 555 014 | send us an email to admin@bricklinegains.com.au</div>
</section>

<section class="testimonial">
  <svg class="arrow" style="left:88px;top:206px" width="14" height="22" viewBox="0 0 14 22" aria-hidden="true"><path d="M11 2 L3 11 L11 20" fill="none" stroke="#d07a28" stroke-width="3"/></svg>
  <svg class="arrow" style="left:1098px;top:206px" width="14" height="22" viewBox="0 0 14 22" aria-hidden="true"><path d="M3 2 L11 11 L3 20" fill="none" stroke="#d07a28" stroke-width="3"/></svg>
  <h2>Mark &amp; Elise,</h2>
  <div class="when">10th November Workshop</div>
  <div class="rule"></div>
  <blockquote>"I would highly recommend people come to this event, the amount of information we have found out has been amazing! We felt very comfortable going through step by step how to renovate each phase and we were very happy with the contacts we made and the people we met."</blockquote>
</section>

<section class="map" role="img" aria-label="Street map of Parramatta showing the event venue"></section>

<footer class="site-footer">
  <div class="brand"><span class="brand-mark"></span>Brickline Gains</div>
  <div class="foot-col" style="left:360px">
    <h4>Contact Us</h4>
    <div class="foot-row">
      <svg width="14" height="14" viewBox="0 0 24 24"><path d="M6.6 10.8c1.4 2.8 3.8 5.1 6.6 6.6l2.2-2.2c.3-.3.7-.4 1-.2 1.1.4 2.3.6 3.6.6.6 0 1 .4 1 1V20c0 .6-.4 1-1 1C10.6 21 3 13.4 3 4c0-.6.4-1 1-1h3.5c.6 0 1 .4 1 1 0 1.3.2 2.5.6 3.6.1.3 0 .7-.2 1z" fill="#d07a28"/></svg>
      1300 555 014</div>
    <div class="foot-row">
      <svg width="14" height="14" viewBox="0 0 24 24"><rect x="3" y="5" width="18" height="14" rx="1" fill="none" stroke="#d07a28" stroke-width="2"/><path d="M3 6 L12 13 L21 6" fill="none" stroke="#d07a28" stroke-width="2"/></svg>
      admin@bricklinegains.com.au</div>
  </div>
  <div class="foot-col" style="left:600px">
    <h4>Event Details</h4>
    <div class="foot-row">
      <svg width="14" height="14" viewBox="0 0 24 24"><rect x="3" y="5" width="18" height="16" rx="1" fill="#d07a28"/><rect x="5" y="10" width="14" height="9" fill="#fff"/></svg>
      Tuesday 2nd May 2017</div>
    <div class="foot-row">
      <svg width="14" height="14" viewBox="0 0 24 24"><circle cx="12" cy="12" r="9" fill="none" stroke="#d07a28" stroke-width="2"/><path d="M12 7 V12 L15 14" fill="none" stroke="#d07a28" stroke-width="2"/></svg>
      7pm to 9pm</div>
    <div class="foot-row">
      <svg width="14" height="14" viewBox="0 0 24 24"><path d="M12 2 C7.6 2 5 5.3 5 9 c0 5 7 13 7 13 s7-8 7-13 c0-3.7-2.6-7-7-7z" fill="#d07a28"/><circle cx="12" cy="9" r="2.5" fill="#fff"/></svg>
      Riverside Grand Parramatta</div>
  </div>
  <a class="btn btn-orange" style="left:850px;top:48px;width:146px;height:32px;font-size:11.5px">Book My Seat Now !</a>
  <div class="partners">Partner Logo's</div>
  <div class="partner-badges"><span></span><span></span><span></span></div>
</footer>

<div class="legal">© 2017 Company Name &nbsp;|&nbsp; All Rights Reserved<span class="page">CS</span></div>

</body>
</html>
```